MSA Plans

I would like to rebuild my brochure for the 3 business plans that I currently offer my clients. I would like to make it look much more modern & attractive to clients when choosing one of our service plans. If we can stick to a tech theme that would be great. Message me for anymore information.

```html
<!DOCTYPE html>
<html lang="en">
<head>
<meta charset="utf-8">
<title>Managed Services Framework – Plan Brochure</title>
<link href="https://fonts.googleapis.com/css2?family=Open+Sans:wght@400;600;700;800&display=swap" rel="stylesheet">
<style>
:root{
  --board:#4b4b4b;
  --orange:#f26522;
  --ink:#111111;
  --paper:#ffffff;
  --line:#8a8a8a;
}
*{box-sizing:border-box;margin:0;padding:0}
html,body{width:1200px;height:676px;overflow:hidden;background:var(--board);font-family:"Open Sans",Arial,sans-serif}
.board{position:relative;width:1200px;height:676px}
.page-label{position:absolute;top:56px;width:354px;text-align:center;color:#fff;font-weight:800;font-size:27px;letter-spacing:.5px}
.sheet{position:absolute;top:111px;width:354px;height:501px;overflow:hidden;box-shadow:0 2px 6px rgba(0,0,0,.35)}
.sheet.cover{left:40px;background:#141414}
.sheet.plans{left:425px;background:var(--paper)}
.sheet.cyber{left:808px;background:var(--paper)}

/* cover */
.cover-art{position:absolute;inset:0 0 64px 0;background:radial-gradient(ellipse at 55% 35%,#3a3a3a 0%,#1c1c1c 55%,#0e0e0e 100%)}
.cover-art::after{content:"";position:absolute;inset:0;background:linear-gradient(135deg,rgba(242,101,34,.18) 0%,rgba(0,0,0,0) 40%,rgba(0,0,0,0) 65%,rgba(242,101,34,.14) 100%)}
.cover-brand{position:absolute;top:186px;left:0;width:100%;text-align:center}
.brand-name{display:inline-flex;align-items:center;gap:6px;font-weight:700;font-size:25px;letter-spacing:2px;color:#fff}
.brand-dot{width:14px;height:14px;border-radius:50%;background:var(--orange)}
.brand-tag{display:block;font-size:5.2px;letter-spacing:1.6px;color:#fff;font-weight:700;margin-top:1px}
.cover-title{position:absolute;top:228px;width:100%;text-align:center;color:var(--orange);font-weight:700;font-size:16.5px}
.cover-version{position:absolute;top:256px;width:100%;text-align:center;color:#fff;font-weight:700;font-size:11px}
.cover-band{position:absolute;top:436px;left:0;width:100%;height:19px;background:var(--orange);color:#fff;font-weight:700;font-size:7.6px;text-align:center;line-height:19px;white-space:nowrap}
.cover-foot{position:absolute;top:455px;left:0;width:100%;background:#141414;height:46px}

.foot{position:absolute;width:100%;text-align:center;font-size:6.9px;line-height:8.4px;color:var(--ink);white-space:nowrap}
.foot .co{color:var(--orange);font-weight:700}
.cover .foot{top:460px;color:#fff}

/* pages */
.head{position:absolute;top:20px;width:100%;text-align:center}
.head .brand-name{color:var(--ink);font-size:17px}
.head .brand-dot{width:11px;height:11px}
.head .brand-tag{color:var(--ink);font-size:3.6px;letter-spacing:1.2px;margin-top:0}
.rule{position:absolute;left:0;width:100%;height:1.5px;background:var(--orange)}
.rule.top{top:54px}
.rule.bottom{top:454px}
.plans .foot,.cyber .foot{top:460px}

.table{position:absolute;top:68px;left:22px;width:308px;font-size:5.5px;color:var(--ink)}
.row{display:grid;height:11.4px;align-items:center;border-bottom:.5px solid var(--line);background:#fff}
.plans .row{grid-template-columns:152px 48px 52px 56px}
.cyber .row{grid-template-columns:200px 52px 56px}
.row > span{height:100%;display:flex;align-items:center;justify-content:center;border-left:.5px solid var(--line);white-space:nowrap;overflow:hidden}
.row > .item{justify-content:flex-start;padding-left:4px}
.cyber .row > .item{font-size:5.2px;letter-spacing:-.05px}
.row > span:last-child{border-right:.5px solid var(--line)}
.row.thead{height:14px;background:var(--ink);color:#fff;font-weight:700;font-size:6.6px;border:none}
.row.thead > span{border:none}
.cyber .row.thead > .item{font-size:6.6px;letter-spacing:0}
.band{height:10.5px;margin-top:1.5px;background:var(--orange);color:#fff;font-weight:700;font-size:6.4px;line-height:10.5px;padding-left:4px}
.price{margin-top:3px}
.price .row{background:var(--ink);height:11.8px;border-bottom:.8px solid #fff;font-weight:700;font-size:6px;color:#fff}
.price .row > span{border-left:.8px solid #fff}
.price .row > .item{color:var(--orange);border-left:none}
.cyber .price .row > .item{font-size:6px}
.price .row > span:last-child{border-right:none}
.ic{width:8px;height:8px}
.lvl{font-size:5px}
sup{font-size:3.5px}
</style>
</head>
<body>
<svg width="0" height="0" style="position:absolute" aria-hidden="true">
  <symbol id="tick" viewBox="0 0 20 20"><circle cx="10" cy="10" r="8.5" fill="none" stroke="#f26522" stroke-width="1.6"/><path d="M6 10.3l2.7 2.7 5.3-5.6" fill="none" stroke="#f26522" stroke-width="1.8" stroke-linecap="round" stroke-linejoin="round"/></symbol>
  <symbol id="cross" viewBox="0 0 20 20"><circle cx="10" cy="10" r="8.5" fill="none" stroke="#111" stroke-width="1.6"/><path d="M7 7l6 6M13 7l-6 6" stroke="#111" stroke-width="1.8" stroke-linecap="round"/></symbol>
</svg>

<main class="board">
  <h2 class="page-label" style="left:40px">MAIN PAGE</h2>
  <h2 class="page-label" style="left:425px">PAGE 1</h2>
  <h2 class="page-label" style="left:808px">PAGE 2</h2>

  <!-- Cover -->
  <section class="sheet cover">
    <div class="cover-art" role="img" aria-label="Dark technology photograph with orange network lines and gear motifs"></div>
    <div class="cover-brand">
      <span class="brand-name"><span class="brand-dot"></span>NORTHGATE</span>
      <span class="brand-tag">YOUR PARTNER FOR EVERY I.T SOLUTION</span>
    </div>
    <h1 class="cover-title">Managed Services Framework</h1>
    <p class="cover-version">Version 1.0 | Updated: April 2024</p>
    <div class="cover-band">DEFINING OUR SERVICES AND HOW WE DELIVER THESE CONSISTENTLY TO YOU.</div>
    <div class="cover-foot"></div>
    <footer class="foot">
      <div class="co">NORTHGATE IT SERVICES PTY LTD | ABN: 41 582 903 116</div>
      <div>northgateit.example | hello@northgateit.example | 1300 555 019</div>
      <div>12/48 Carrow St, Brookvale, VIC, 3150</div>
    </footer>
  </section>

  <!-- Page 1 -->
  <section class="sheet plans">
    <header class="head">
      <span class="brand-name"><span class="brand-dot"></span>NORTHGATE</span>
      <span class="brand-tag">YOUR PARTNER FOR EVERY I.T SOLUTION</span>
    </header>
    <div class="rule top"></div>

    <div class="table">
      <div class="row thead"><span class="item">Managed Services Agreement</span><span>Essential</span><span>Business</span><span>Professional</span></div>

      <div class="band">Support</div>
      <div class="row"><span class="item">Unlimited Remote Support 7am to 6pm</span><span><svg class="ic"><use href="#tick"/></svg></span><span><svg class="ic"><use href="#tick"/></svg></span><span><svg class="ic"><use href="#tick"/></svg></span></div>
      <div class="row"><span class="item">3<sup>rd</sup>&nbsp;Party Vendor Support</span><span><svg class="ic"><use href="#tick"/></svg></span><span><svg class="ic"><use href="#tick"/></svg></span><span><svg class="ic"><use href="#tick"/></svg></span></div>
      <div class="row"><span class="item">Reactive Onsite Support 8am to 5pm</span><span>VIP Rates</span><span><svg class="ic"><use href="#tick"/></svg></span><span><svg class="ic"><use href="#tick"/></svg></span></div>
      <div class="row"><span class="item">After-Hours Support</span><span>VIP Rates</span><span>VIP Rates</span><span><svg class="ic"><use href="#tick"/></svg></span></div>

      <div class="band">Service</div>
      <div class="row"><span class="item">Guaranteed SLA Response Times</span><span><svg class="ic"><use href="#tick"/></svg></span><span><svg class="ic"><use href="#tick"/></svg></span><span><svg class="ic"><use href="#tick"/></svg></span></div>
      <div class="row"><span class="item">24x7 Website &amp; Infrastructure Monitoring</span><span><svg class="ic"><use href="#tick"/></svg></span><span><svg class="ic"><use href="#tick"/></svg></span><span><svg class="ic"><use href="#tick"/></svg></span></div>
      <div class="row"><span class="item">Secure Web Content Filtering</span><span><svg class="ic"><use href="#tick"/></svg></span><span><svg class="ic"><use href="#tick"/></svg></span><span><svg class="ic"><use href="#tick"/></svg></span></div>
      <div class="row"><span class="item">Backup Monitoring</span><span><svg class="ic"><use href="#tick"/></svg></span><span><svg class="ic"><use href="#tick"/></svg></span><span><svg class="ic"><use href="#tick"/></svg></span></div>
      <div class="row"><span class="item">Desktop OS Patching &amp; Updating</span><span><svg class="ic"><use href="#tick"/></svg></span><span><svg class="ic"><use href="#tick"/></svg></span><span><svg class="ic"><use href="#tick"/></svg></span></div>
      <div class="row"><span class="item">CEO / MD Home Tech Support</span><span><svg class="ic"><use href="#tick"/></svg></span><span><svg class="ic"><use href="#tick"/></svg></span><span><svg class="ic"><use href="#tick"/></svg></span></div>
      <div class="row"><span class="item">Monthly Tech Site Visit</span><span><svg class="ic"><use href="#cross"/></svg></span><span>Quarterly</span><span>Monthly</span></div>
      <div class="row"><span class="item">Short Term Loan Equipment</span><span><svg class="ic"><use href="#cross"/></svg></span><span>1 Month</span><span>3 Months</span></div>
      <div class="row"><span class="item">Adds / Moves / Changes (Staff)</span><span><svg class="ic"><use href="#tick"/></svg></span><span><svg class="ic"><use href="#tick"/></svg></span><span><svg class="ic"><use href="#tick"/></svg></span></div>
      <div class="row"><span class="item">Adds / Moves / Changes (Workstations)</span><span>VIP Rates</span><span>VIP Rates</span><span><svg class="ic"><use href="#tick"/></svg></span></div>

      <div class="band">Management</div>
      <div class="row"><span class="item">Asset and Warranty Tracking &amp; Reporting</span><span><svg class="ic"><use href="#tick"/></svg></span><span><svg class="ic"><use href="#tick"/></svg></span><span><svg class="ic"><use href="#tick"/></svg></span></div>
      <div class="row"><span class="item">Comprehensive IT Documentation</span><span><svg class="ic"><use href="#tick"/></svg></span><span><svg class="ic"><use href="#tick"/></svg></span><span><svg class="ic"><use href="#tick"/></svg></span></div>
      <div class="row"><span class="item">Technology Strategy Meeting</span><span>Annual</span><span>Quarterly</span><span>Monthly</span></div>
      <div class="row"><span class="item">Technology Business Review Meeting</span><span>Annual</span><span>Bi Annual</span><span>Quarterly</span></div>
      <div class="row"><span class="item">IT Policy Templates</span><span><svg class="ic"><use href="#cross"/></svg></span><span><svg class="ic"><use href="#tick"/></svg></span><span><svg class="ic"><use href="#tick"/></svg></span></div>

      <div class="band">Training</div>
      <div class="row"><span class="item">End User Training Materials</span><span><svg class="ic"><use href="#cross"/></svg></span><span><svg class="ic"><use href="#cross"/></svg></span><span><svg class="ic"><use href="#tick"/></svg></span></div>
      <div class="row"><span class="item">Security Awareness Training</span><span><svg class="ic"><use href="#tick"/></svg></span><span><svg class="ic"><use href="#tick"/></svg></span><span><svg class="ic"><use href="#tick"/></svg></span></div>

      <div class="price">
        <div class="row"><span class="item">RRP / User</span><span>$110</span><span>$130</span><span>$165</span></div>
        <div class="row"><span class="item">Minimum User Count</span><span>5</span><span>5</span><span>5</span></div>
        <div class="row"><span class="item">Minimum Monthly Commit</span><span>$550</span><span>$650</span><span>$825</span></div>
      </div>
    </div>

    <div class="rule bottom"></div>
    <footer class="foot">
      <div class="co">NORTHGATE IT SERVICES PTY LTD | ABN: 41 582 903 116</div>
      <div>northgateit.example | hello@northgateit.example | 1300 555 019</div>
      <div>12/48 Carrow St, Brookvale, VIC, 3150</div>
    </footer>
  </section>

  <!-- Page 2 -->
  <section class="sheet cyber">
    <header class="head">
      <span class="brand-name"><span class="brand-dot"></span>NORTHGATE</span>
      <span class="brand-tag">YOUR PARTNER FOR EVERY I.T SOLUTION</span>
    </header>
    <div class="rule top"></div>

    <div class="table">
      <div class="row thead"><span class="item">Cybersecurity Packages</span><span>Business</span><span>Professional</span></div>
      <div class="row" style="height:12.5px"><span class="item">Compliance with NCSB Baseline 8 Maturity</span><span class="lvl">Level 0</span><span class="lvl">Level 1</span></div>
      <div class="row"><span class="item">Security Standard - Alignment to Northgate 365 Security Policy &amp; Reporting</span><span><svg class="ic"><use href="#tick"/></svg></span><span><svg class="ic"><use href="#tick"/></svg></span></div>
      <div class="row"><span class="item">24x7 Security Operations Centre (SOC) - Monitoring Cloud Suite</span><span><svg class="ic"><use href="#tick"/></svg></span><span><svg class="ic"><use href="#tick"/></svg></span></div>
      <div class="row"><span class="item">Dark Web Scanning</span><span><svg class="ic"><use href="#tick"/></svg></span><span><svg class="ic"><use href="#tick"/></svg></span></div>
      <div class="row"><span class="item">Cloud Email Filtering</span><span><svg class="ic"><use href="#tick"/></svg></span><span><svg class="ic"><use href="#tick"/></svg></span></div>
      <div class="row"><span class="item">Cloud Mailbox Backup</span><span><svg class="ic"><use href="#tick"/></svg></span><span><svg class="ic"><use href="#tick"/></svg></span></div>
      <div class="row"><span class="item">Automated Email Signatures</span><span><svg class="ic"><use href="#tick"/></svg></span><span><svg class="ic"><use href="#tick"/></svg></span></div>
      <div class="row"><span class="item">Endpoint Protection with EDR - Workstations &amp; Servers</span><span><svg class="ic"><use href="#tick"/></svg></span><span><svg class="ic"><use href="#tick"/></svg></span></div>
      <div class="row"><span class="item">3rd Party Applications Updating</span><span><svg class="ic"><use href="#cross"/></svg></span><span><svg class="ic"><use href="#tick"/></svg></span></div>
      <div class="row"><span class="item">24x7 Security Operations Centre (SOC) - Monitoring Endpoints and Servers</span><span><svg class="ic"><use href="#cross"/></svg></span><span><svg class="ic"><use href="#tick"/></svg></span></div>
      <div class="row"><span class="item">Privileged Access Management &amp; Application Whitelisting</span><span><svg class="ic"><use href="#cross"/></svg></span><span><svg class="ic"><use href="#tick"/></svg></span></div>
      <div class="row"><span class="item">Internal Vulnerability Scanning</span><span><svg class="ic"><use href="#cross"/></svg></span><span><svg class="ic"><use href="#tick"/></svg></span></div>
      <div class="row"><span class="item">Backup &amp; Disaster Recovery to comply with NCSB Baseline 8 Maturity</span><span><svg class="ic"><use href="#cross"/></svg></span><span class="lvl">Pending Assessment</span></div>

      <div class="price">
        <div class="row"><span class="item">RRP / User</span><span>$35</span><span>$60</span></div>
        <div class="row"><span class="item">Minimum User Count</span><span>5</span><span>5</span></div>
        <div class="row"><span class="item">Minimum Monthly Commit</span><span>$175</span><span>$300</span></div>
      </div>
    </div>

    <div class="rule bottom"></div>
    <footer class="foot">
      <div class="co">NORTHGATE IT SERVICES PTY LTD | ABN: 41 582 903 116</div>
      <div>northgateit.example | hello@northgateit.example | 1300 555 019</div>
      <div>12/48 Carrow St, Brookvale, VIC, 3150</div>
    </footer>
  </section>
</main>
</body>
</html>
```